Healthy juice company needs a branded shipping box

I am looking for a branded box that is 10"x10"x10" in standard brown. This is for the box we ship the juice in.

The box should serve as an advertising platform in itself. We offer a subscription juice service. People get a box of juice delivered every week.

The customer should see the box and feel good about what they ordered because it's something healthy they're doing for themselves. The imagery/wording should reinforce that they're doing something healthy for themselves.

Other people who see the box should be curious enough to look us up and want a box for themselves.

I'd like ONE color in the final print.

I'd like the 4 sides of the box to be printed.

The design is up to you.

Inspiration boxes: Amber Ladle, Tidy Basket, PrintHollow

Target Market(s)

Our customers subscribe to our juice because it helps them eat the fruits and veggies they normally wouldn't. They are typically 30-40yrs old, with families, and are upper middle class.

Industry/Entity Type

Delivery Service

Font styles to use
Sans Serif

Colors
f78f20
9bcb3c
ffffff

Requirements
Must have
• The design should feel clean, bright, happy, casual, and healthy.
• Natural fruits & veggies are part of what we do.
• Has to convey farm fresh, fresh made and locally made through the design.
• Must have website: www.varolipressery.example
Nice to have
• These can optionally be included on the box:
• - "I care about my health."
• - "Drink Juice. Live Healthier."
• The box can be branded "The Pulp Crate" on 1+ sides

```html
<!DOCTYPE html>
<html lang="en">
<head>
<meta charset="utf-8">
<title>Varoli Pressery – The Pulp Crate shipping box dieline</title>
<link rel="stylesheet" href="https://fonts.googleapis.com/css2?family=Comfortaa:wght@500&family=Dancing+Script:wght@700&family=Montserrat:wght@500;700&display=swap">
<style>
  :root {
    --kraft: #b08a6a;
    --ink: #2c6446;
    --ink-soft: rgba(44,100,70,0.42);
    --ink-faint: rgba(44,100,70,0.18);
    --paper: #ffffff;
    --fold: rgba(255,255,255,0.45);
  }
  * { margin: 0; padding: 0; box-sizing: border-box; }
  html, body { width: 1121px; height: 1200px; overflow: hidden; background: var(--paper); }
  .canvas { position: relative; width: 1121px; height: 1200px; }

  .panel { position: absolute; width: 237px; background: var(--kraft); color: var(--ink); }
  .panel--front-a { left: 79px;  top: 606px; height: 474px; }
  .panel--side-a  { left: 316px; top: 622px; height: 426px; }
  .panel--front-b { left: 553px; top: 606px; height: 474px; }
  .panel--side-b  { left: 790px; top: 622px; height: 422px; }

  .fold { position: absolute; left: 0; right: 0; height: 1px; background: var(--fold); }
  .panel--front-a .fold--top, .panel--front-b .fold--top { top: 118px; }
  .panel--side-a .fold--top, .panel--side-b .fold--top { top: 102px; }

  .face { position: absolute; left: 0; right: 0; height: 238px; }
  .panel--front-a .face, .panel--front-b .face { top: 118px; }
  .panel--side-a .face, .panel--side-b .face { top: 102px; }

  .claims { position: absolute; left: 0; right: 0; top: 44px; height: 40px; }
  .claim { position: absolute; width: 54px; margin-left: -27px; text-align: center; }
  .claim__label { display: block; font: 500 4px/1 "Montserrat", sans-serif; transform: rotate(180deg); margin-bottom: 7px; }
  .claim__icon { display: block; width: 14px; height: 14px; margin: 0 auto; }

  .badge { position: absolute; left: 13px; top: 14px; width: 23px; height: 23px; border-radius: 50%; border: 1.5px solid var(--ink); }

  .handling { position: absolute; right: 8px; top: 8px; display: flex; gap: 4px; align-items: flex-start; font-family: "Montserrat", sans-serif; }
  .handling svg { width: 18px; height: 14px; }
  .handling__text { font-size: 4px; line-height: 1.25; }
  .handling__text strong { display: block; font-size: 5px; }
  .panel--front-b .handling { right: 14px; top: 10px; }
  .panel--front-b .handling__text { font-size: 6px; }
  .panel--front-b .handling__text strong { font-size: 6px; border-bottom: 1.5px solid var(--ink); }
  .panel--front-b .handling svg { width: 20px; height: 15px; }

  .brand { position: absolute; left: 0; right: 0; top: 66px; display: flex; align-items: center; justify-content: center; gap: 7px; }
  .brand__dot { width: 10px; height: 10px; border-radius: 50%; background: var(--ink); }
  .brand__name { font: 500 24px/1 "Comfortaa", sans-serif; letter-spacing: .3px; }

  .tagline { position: absolute; left: 0; right: 0; top: 156px; text-align: center; font: 700 17px/1 "Dancing Script", cursive; }

  .band { position: absolute; left: 0; right: 0; bottom: 0; height: 56px; }
  .band svg { position: absolute; inset: 0; width: 100%; height: 100%; }
  .band__url { position: absolute; left: 0; right: 0; bottom: 15px; text-align: center; color: var(--paper); font: 500 8px/1 "Montserrat", sans-serif; letter-spacing: .3px; }

  .wreath { position: absolute; left: 18px; top: 14px; width: 202px; height: 202px; border-radius: 50%;
    background: radial-gradient(circle,
      transparent 0 44%,
      var(--ink-faint) 50%,
      var(--ink-soft) 62%,
      var(--ink-soft) 84%,
      var(--ink-faint) 94%,
      transparent 100%); }
  .wreath__title { position: absolute; left: 0; right: 0; top: 72px; text-align: center; font: 700 27px/.95 "Dancing Script", cursive; }
</style>
</head>
<body>
<main class="canvas">

  <section class="panel panel--front-a">
    <div class="claims">
      <div class="claim" style="left:29px"><span class="claim__label">No Additives</span>
        <svg class="claim__icon" viewBox="0 0 14 14"><circle cx="7" cy="7" r="6" fill="none" stroke="#2c6446"/><path d="M4 4l6 6" stroke="#2c6446"/></svg></div>
      <div class="claim" style="left:82px"><span class="claim__label">Fully Recyclable</span>
        <svg class="claim__icon" viewBox="0 0 14 14"><path d="M7 2l5 9H2z" fill="none" stroke="#2c6446"/></svg></div>
      <div class="claim" style="left:124px"><span class="claim__label">No Sugar</span>
        <svg class="claim__icon" viewBox="0 0 14 14"><circle cx="7" cy="7" r="6" fill="none" stroke="#2c6446"/></svg></div>
      <div class="claim" style="left:175px"><span class="claim__label">Non GMO</span>
        <svg class="claim__icon" viewBox="0 0 14 14"><circle cx="7" cy="7" r="6" fill="none" stroke="#2c6446"/></svg></div>
    </div>
    <div class="fold fold--top"></div>
    <div class="face">
      <div class="badge" aria-hidden="true"></div>
      <div class="handling">
        <svg viewBox="0 0 18 14"><path d="M5 13V3M2 6l3-4 3 4M13 13V3M10 6l3-4 3 4M1 13h16" fill="none" stroke="#2c6446" stroke-width="1.5"/></svg>
        <div class="handling__text">This Way Up<strong>PERISHABLE</strong>Keep Cold</div>
      </div>
      <div class="brand"><span class="brand__dot"></span><span class="brand__name">Varoli Pressery</span></div>
      <p class="tagline">The Pulp Crate</p>
      <div class="band">
        <svg viewBox="0 0 237 56" preserveAspectRatio="none"><path d="M0 14 C60 0 120 10 170 12 C200 13 222 8 237 0 V56 H0Z" fill="#2c6446"/></svg>
        <p class="band__url">www.varolipressery.example</p>
      </div>
    </div>
  </section>

  <section class="panel panel--side-a">
    <div class="fold fold--top"></div>
    <div class="face">
      <div class="wreath" role="img" aria-label="Line-drawn wreath of fruits and vegetables framing the words Farm Fresh">
        <p class="wreath__title">Farm<br>Fresh</p>
      </div>
    </div>
  </section>

  <section class="panel panel--front-b">
    <div class="fold fold--top"></div>
    <div class="face">
      <div class="handling">
        <svg viewBox="0 0 18 14"><path d="M5 13V3M2 6l3-4 3 4M13 13V3M10 6l3-4 3 4" fill="none" stroke="#2c6446" stroke-width="1.8"/></svg>
        <div class="handling__text">This Way Up<strong>PERISHABLE</strong></div>
      </div>
      <div class="brand"><span class="brand__dot"></span><span class="brand__name">Varoli Pressery</span></div>
      <p class="tagline">The Pulp Crate</p>
      <div class="band">
        <svg viewBox="0 0 237 56" preserveAspectRatio="none"><path d="M0 14 C60 0 120 10 170 12 C200 13 222 8 237 0 V56 H0Z" fill="#2c6446"/></svg>
        <p class="band__url">www.varolipressery.example</p>
      </div>
    </div>
  </section>

  <section class="panel panel--side-b">
    <div class="fold fold--top"></div>
    <div class="face">
      <div class="wreath" role="img" aria-label="Line-drawn wreath of fruits and vegetables framing the words Farm Fresh">
        <p class="wreath__title">Farm<br>Fresh</p>
      </div>
    </div>
  </section>

</main>
</body>
</html>
```